Veloran Dental Development - Business Cards

We are a Dental Development and Management company. We are looking to develop a new business card design. We are business professional but modern. The logo that I have attached is the business colors. You can also check out our website for further detail. www.veloranmgmt-example.com

Target Market(s)

Dental Professionals, Dentists and Office Staff, Marketing Professionals

Industry/Entity Type

Business

Requirements
Must have
• Name - Bartholomew K. Tressing
Title - Marketing Director
Phone - 555-019-4827
Cell - 555-019-4827
Email - Bart.t@veloran-example.com
Address - 2917 W Larkmoor Rd, Mesa, AZ 85209
Web- www.veloran-example.com

Veloran Logo must go on the front. The other logos go on the back as affiliated businesses

Must be editable to enter specific Names, Positions, Phone numbers and email later on. Using Adobe CS5 currently.

```html
<!DOCTYPE html>
<html lang="en">
<head>
<meta charset="utf-8">
<title>Veloran Dental Development – Business Cards</title>
<link href="https://fonts.googleapis.com/css2?family=Libre+Baskerville:wght@400;700&family=Tinos:wght@400&display=swap" rel="stylesheet">
<style>
  :root{
    --stage:#434848;
    --paper:#ffffff;
    --navy:#23265e;
    --navy-deep:#05061a;
    --gold:#c98d22;
    --gold-dark:#8a5a10;
    --grey-text:#555555;
  }
  *{margin:0;padding:0;box-sizing:border-box}
  html,body{width:1200px;height:1200px;overflow:hidden}
  body{background:var(--stage);position:relative;font-family:"Tinos",serif}
  .card{position:absolute;top:445px;width:517px;height:310px;background:var(--paper);overflow:hidden}
  .card--front{left:50px}
  .card--back{left:633px}

  .band-gold{position:absolute;left:0;right:0;height:22px;
    background:linear-gradient(180deg,#a86c12 0%,var(--gold) 45%,#b67914 75%,var(--gold-dark) 100%)}
  .band-navy{position:absolute;left:0;right:0;height:34px;
    background:linear-gradient(180deg,#1c2160 0%,var(--navy-deep) 55%,#000 100%)}

  /* front */
  .card--front .band-gold{top:254px}
  .card--front .band-navy{top:276px}
  .brand-name{position:absolute;top:74px;left:0;right:0;text-align:center;
    font-family:"Libre Baskerville",serif;font-weight:700;font-size:27px;color:var(--navy);letter-spacing:.5px}
  .brand-name .brand-dot{display:inline-block;width:14px;height:14px;border-radius:50%;background:var(--gold);margin-right:10px;vertical-align:2px}
  .person{position:absolute;top:189px;left:0;right:0;text-align:center;
    font-family:"Libre Baskerville",serif;font-weight:700;font-size:16px;color:var(--navy)}
  .person .initial{color:var(--gold)}
  .role{position:absolute;top:210px;left:0;right:0;text-align:center;font-size:13px;color:var(--grey-text)}
  .address{position:absolute;top:236px;left:0;right:0;text-align:center;font-size:12px;letter-spacing:2.6px;color:var(--grey-text)}
  .contact{position:absolute;top:254px;left:0;right:0;height:22px;display:flex;justify-content:center;align-items:center;gap:12px;
    font-size:12.5px;color:#fff}
  .contact-item{display:flex;align-items:center;gap:4px}
  .contact-item svg{width:14px;height:14px}

  /* back */
  .card--back .band-navy{top:0}
  .card--back .band-gold{top:33px;height:23px}
  .web{position:absolute;top:33px;left:0;right:0;height:23px;line-height:23px;text-align:center;
    font-size:11.5px;letter-spacing:5.2px;color:#fff}
  .affiliate-art{position:absolute;left:30px;top:87px;width:226px;height:183px}
  .affiliate{position:absolute;left:287px;width:200px;text-align:center;font-family:"Libre Baskerville",serif;font-weight:700;font-size:17px;line-height:1.25}
  .affiliate--centers{top:108px;color:#1d5e86}
  .affiliate--plan{top:212px;color:#9b2a1c}
</style>
</head>
<body>

<section class="card card--front">
  <div class="brand-name"><span class="brand-dot"></span>Veloran Dental Development</div>
  <div class="person">Bartholomew <span class="initial">K.</span> Tressing</div>
  <div class="role">Marketing Director</div>
  <div class="address">2917 W Larkmoor Rd, Mesa, AZ 85209</div>
  <div class="band-gold"></div>
  <div class="contact">
    <span class="contact-item">
      <svg viewBox="0 0 14 14"><rect width="14" height="14" rx="2" fill="#1a1a1a"/><path d="M4 3.5c.8-.6 1.4-.3 1.7.4l.4 1c.2.5 0 .9-.4 1.2.4.9 1 1.6 1.9 2.1.3-.4.7-.6 1.2-.4l1 .4c.7.3.9.9.3 1.7-1.8 1.6-7.4-3.7-6.1-6.4z" fill="#fff"/></svg>
      555-019-4827
    </span>
    <span class="contact-item">
      <svg viewBox="0 0 14 14"><rect width="14" height="14" rx="2" fill="#1a1a1a"/><rect x="4.5" y="2" width="5" height="10" rx="1" fill="#fff"/><rect x="5.3" y="3" width="3.4" height="5" fill="#1a1a1a"/></svg>
      555-019-4827
    </span>
    <span class="contact-item">
      <svg viewBox="0 0 14 14"><rect width="14" height="14" rx="2" fill="#1a1a1a"/><rect x="2.5" y="4" width="9" height="6.5" fill="#fff"/><path d="M2.5 4l4.5 3.5L11.5 4" fill="none" stroke="#1a1a1a" stroke-width="1"/></svg>
      Bart.t@veloran-example.com
    </span>
  </div>
  <div class="band-navy"></div>
</section>

<section class="card card--back">
  <div class="band-navy"></div>
  <div class="band-gold"></div>
  <div class="web">www.veloran-example.com</div>
  <div class="affiliate-art" role="img" aria-label="Brightbud Pediatric Dental affiliate badge"
       style="background:radial-gradient(ellipse at center,#f5e23a 0%,#f08a1e 45%,#2fb4e4 75%,rgba(255,255,255,0) 100%)"></div>
  <div class="affiliate affiliate--centers">Hearthside<br>Dental Centers</div>
  <div class="affiliate affiliate--plan">Hearthside<br>Dental Plan</div>
</section>

</body>
</html>
```